Tuck Away! Flyer Design - Double Sided, Get Creative!

We are looking for a flexible flyer design, DL sized print.

We are launching a new service - Tuck Away! - which is basically a personal, urban self storage solution. We deliver boxes, our customer pack them, we collect and store and can re-deliver on demand.

For colour, logo and a better idea of the service please see our website www.simplytuckaway.com.au

One side of the flyer will need a picture of the box, explanation of the service, a call to action with an offer, as well as a price. The tag line is Simply Tuck AWAY!

The other side is where we need creative input. We are looking for something clean and modern, that appeals to a market 18 - 45. I am happy to explore the idea of multiple different concepts to target each market (ie. one targeting mothers, one targeting students, etc) and will pay for each of those if the concept is good.

Our target market is apartment dwellers, students, mothers with young children (but who have outgrown toys, etc), older people whose kids have left home, and people moving to smaller houses from larger ones.

The value proposition of our service is that:

1, Very cost effective
2 .Very convenient (delivered to/from your door)
3. No wasted space, so not wasting money

Please take inspiration from our website for font and colours.
Updates

Hi All,Just wanted to add that we are also going to need other collateral once this is done - posters, etc. So please think of this as more than just a one off job! Added Tuesday, February 24, 2015

Target Market(s)

People looking for storage of items / stuff. Our target market is apartment dwellers, students, mothers with young children (but who have outgrown toys, etc), older people whose kids have left home, and people moving to smaller houses from larger ones.

Industry/Entity Type

Self Storage

Font styles to use
Sans Serif

Requirements
Must have
• Our logo, a picture of our box, our value propositions, how the service works, call to action / offer.
• Side 1: Communicate the Idea of storage, mess - tidy. Maybe a cover to target each market vertical.
• Side 2: Picture of our box, our value propositions, how the service works, call to action / offer.
Nice to have
• Idea of mess -> tidy, etc.

```html
<!DOCTYPE html>
<html lang="en">
<head>
<meta charset="utf-8">
<title>Tuck Away! Flyer – Front and Back</title>
<link rel="stylesheet" href="https://fonts.googleapis.com/css2?family=Roboto+Condensed:wght@300;400;700&family=Russo+One&display=swap">
<style>
  :root{
    --blue:#2aa3dc;
    --blue-dark:#1f8cc4;
    --navy:#33475b;
    --red:#b8302a;
    --white:#ffffff;
    --ink:#2b3a48;
    --page:#e4e6e8;
  }
  *{box-sizing:border-box;margin:0;padding:0}
  html,body{width:1200px;height:905px;overflow:hidden}
  body{background:var(--page);font-family:"Roboto Condensed",Arial,sans-serif;color:var(--ink);position:relative}

  .flyer{position:absolute;background:var(--white);box-shadow:0 3px 10px rgba(0,0,0,.25);overflow:hidden}
  .flyer--front{left:113px;top:64px;width:382px;height:790px}
  .flyer--back{left:637px;top:122px;width:371px;height:765px}
  .abs{position:absolute}

  /* brand lockup */
  .brand{display:flex;align-items:center;gap:10px;color:var(--blue);font-weight:700;white-space:nowrap}
  .brand__square{background:var(--blue);display:block}
  .brand--large{left:40px;top:20px;font-size:56px;letter-spacing:1px}
  .brand--large .brand__square{width:22px;height:22px}
  .brand--small{left:14px;top:733px;font-size:24px;gap:6px}
  .brand--small .brand__square{width:10px;height:10px}
  .brand__sub{position:absolute;left:252px;top:80px;font-size:12px;color:var(--blue);letter-spacing:.5px}

  /* front */
  .front__heading{left:0;top:114px;width:100%;text-align:center;color:var(--red);font-size:17px;font-weight:400}
  .front__intro{left:27px;top:138px;width:330px;font-size:13.5px;line-height:1.4;text-align:justify;font-weight:300;color:#222}
  .front__band{left:0;top:240px;width:382px;height:345px}
  .photo{left:50px;top:268px;width:310px;height:198px;background:linear-gradient(150deg,#c98f8f 0%,#8d7aa0 25%,#2f8fcf 55%,#1b6ea6 100%);border-radius:4px}
  .price{left:28px;top:268px;width:52px;height:52px;background:var(--red);color:var(--white);border-radius:8px 26px 26px 26px;text-align:center;padding-top:8px;box-shadow:0 2px 4px rgba(0,0,0,.3)}
  .price__from{font-size:10px;font-style:italic;display:block}
  .price__amount{font-size:17px;font-weight:700;line-height:1}
  .step{font-size:10px;color:var(--ink);text-align:center}
  .step svg{display:block;margin:4px auto 0}
  .step--deliver{left:254px;top:236px}
  .step--pack{left:326px;top:236px}
  .step--collect{left:30px;top:503px}
  .step--return{left:130px;top:503px}
  .step__figure{display:block;margin:4px auto 0;width:34px;height:32px;background:var(--white);opacity:.85;border-radius:3px}
  .value__lead{left:30px;top:559px;color:var(--red);font-size:15px}
  .front__navy{left:0;top:584px;width:100%;height:164px;background:var(--navy)}
  .value__list{left:30px;top:591px;list-style:none;color:var(--white);font-size:15px;line-height:24px;font-weight:300}
  .tagline{font-family:"Russo One",Arial,sans-serif;color:var(--white);white-space:nowrap;text-align:center;width:100%;left:0}
  .tagline--front{top:670px;font-size:32px}
  .footer{left:0;width:100%;background:var(--white);text-align:center;color:#111;font-weight:700;font-size:15px;line-height:19px}
  .footer--front{top:748px;height:42px;padding-top:3px}

  /* back */
  .back__blue{left:0;top:0;width:100%;background:var(--blue)}
  .back__blue--top{height:270px}
  .back__blue--pricing{top:482px;height:86px}
  .rule{left:0;width:100%;height:4px;background:var(--white)}
  .back__title{left:0;width:100%;text-align:center;color:var(--red);font-size:17px;line-height:22px;font-weight:400}
  .back__text{left:24px;width:336px;color:var(--white);font-size:14px;line-height:19px;font-weight:300}
  .bullets{left:14px;width:350px;list-style:none;font-size:11px;line-height:15.5px;font-weight:300;white-space:nowrap}
  .bullets li::before{content:"•";color:var(--red);margin-right:3px}
  .bullets--light{color:var(--white)}
  .bullets--dark{color:#222}
  .back__text--dark{color:#222}
  .back__note{left:0;width:100%;text-align:center;font-size:12px;color:var(--ink);font-weight:300}
  .pricing__row{left:24px;width:330px;display:flex;justify-content:space-between;color:#0d2a40;font-size:11.5px}
  .back__navy{left:0;top:568px;width:100%;height:152px;background:var(--navy)}
  .contact{color:var(--white);font-size:14px;line-height:19px;font-weight:300;display:flex;gap:7px;white-space:nowrap}
  .contact svg{flex:none;margin-top:4px}
  .contact--address{left:40px;top:584px}
  .contact--mail{left:188px;top:585px;font-size:13px}
  .contact--social{left:188px;top:620px;font-size:13px}
  .tagline--back{top:650px;font-size:30px}
  .footer--back{top:720px;height:45px;text-align:right;padding:5px 14px 0 0;font-size:13px;line-height:17px}
  .footer--back span{display:block;text-align:center;margin-left:auto;width:190px}
</style>
</head>
<body>

<section class="flyer flyer--front" aria-label="Flyer front">
  <div class="abs brand brand--large"><span class="brand__square"></span>Tuck Away!</div>
  <div class="abs brand__sub">URBAN STORAGE</div>

  <h2 class="abs front__heading">Self Storage by the Box Delivered to your Door.</h2>
  <p class="abs front__intro">We have redefined self storage for the modern urban world. No more schlepping to outer suburbs to store away or retrieve your belongings; no more paying for space that you dont need.With Tuck Away! you only pay for what you need, and we deliver to your door.</p>

  <svg class="abs front__band" viewBox="0 0 382 345" width="382" height="345">
    <rect x="0" y="0" width="382" height="345" fill="var(--blue)"/>
    <polygon points="0,8 382,84 382,88 0,12" fill="var(--white)"/>
    <polygon points="0,18 382,94 382,305 0,218" fill="var(--white)"/>
    <polygon points="0,226 382,313 382,317 0,230" fill="var(--white)"/>
    <polygon points="0,290 382,332 382,345 0,345" fill="var(--blue-dark)" opacity=".35"/>
  </svg>

  <div class="abs photo" role="img" aria-label="Two open blue storage boxes filled with folded clothes, with a soft toy beside them"></div>

  <div class="abs price"><span class="price__from">from</span><span class="price__amount">$5.95</span></div>

  <div class="abs step step--deliver">We Deliver
    <svg width="30" height="34" viewBox="0 0 30 34"><rect x="3" y="1" width="24" height="22" rx="2" fill="#fff"/><rect x="6" y="5" width="18" height="8" fill="var(--blue)"/><rect x="1" y="23" width="28" height="6" fill="#fff"/><circle cx="8" cy="31" r="3" fill="#fff"/><circle cx="22" cy="31" r="3" fill="#fff"/></svg>
  </div>
  <div class="abs step step--pack">You Pack
    <svg width="34" height="30" viewBox="0 0 34 30"><path d="M3 10h28v18H3z" fill="#fff"/><path d="M5 8l4-7h12l2 4h6l2 3z" fill="#fff"/><path d="M3 10h28" stroke="var(--blue)" stroke-width="1.5"/></svg>
  </div>
  <div class="abs step step--collect">We Collect &amp; Store<span class="step__figure" role="img" aria-label="Person wheeling boxes to storage shelves"></span></div>
  <div class="abs step step--return">We Return<span class="step__figure" role="img" aria-label="Person delivering boxes on a trolley to a customer"></span></div>

  <p class="abs value__lead">The value proposition of our service is that:</p>

  <div class="abs front__navy"></div>
  <ol class="abs value__list">
    <li>1. Very cost effective</li>
    <li>2. Very convenient (delivered to/from your door)</li>
    <li>3. No wasted space, so not wasting money</li>
  </ol>
  <p class="abs tagline tagline--front">Simply Tuck AWAY!</p>
  <div class="abs footer footer--front">WWW.SIMPLYTUCKAWAY.COM.AU<br>1300 482 615</div>
</section>

<section class="flyer flyer--back" aria-label="Flyer back">
  <div class="abs back__blue back__blue--top"></div>
  <h2 class="abs back__title" style="top:12px">Security &amp; Insurance<br>Business grade security for your belongings</h2>
  <p class="abs back__text" style="top:74px">Our facility is also used for commercial storage, which means that your precious goods are in very good company.</p>
  <p class="abs back__text" style="top:131px">We offer business grade security and safety features - a major piont of difference.</p>
  <ul class="abs bullets bullets--light" style="top:172px">
    <li>Tier 1 Secure facility with restricted access control</li>
    <li>24/7 CCTV / Alarm Monitored</li>
    <li>Fully Sprinklered and fire monitored</li>
    <li>Unique Security Seals on each Box to ensure tampering</li>
    <li>All boxes tracked via barcode</li>
    <li>Complimentary insurance for your belongings of up to $150 per Tuck Away Box</li>
  </ul>
  <div class="abs rule" style="top:270px"></div>

  <h2 class="abs back__title" style="top:283px">Tuck Away Box</h2>
  <p class="abs back__text back__text--dark" style="top:326px">Only pay for the boxes you use. Order more than you think - any empties we will credit back to you!</p>
  <ul class="abs bullets bullets--dark" style="top:367px">
    <li>FREE Delivery of your empty boxes</li>
    <li>FREE Pickup of your full boxes to go to storage</li>
    <li>1 Week to pack your boxes. After this, your storage period starts</li>
    <li>2 Tamper Evident Seals per box</li>
    <li>Up to $150 contents insurance cover per box</li>
  </ul>
  <p class="abs back__note" style="top:456px">Delivery of your full boxes: $15 per delivery + $2 per box</p>

  <div class="abs back__blue back__blue--pricing"></div>
  <div class="abs rule" style="top:476px"></div>
  <h2 class="abs back__title" style="top:486px">Simple As Pricing</h2>
  <p class="abs back__text" style="top:507px">Only pay for what you need. MUCH more cost effective than self storage.</p>
  <div class="abs pricing__row" style="top:546px"><span>FROM $14 PER ITEM PER MONTH</span><span>$5.95 PER BOX PER 4 WEEKS</span></div>

  <div class="abs back__navy"></div>
  <div class="abs contact contact--address">
    <svg width="10" height="10" viewBox="0 0 10 10"><path d="M10 0L0 4l4 2 2 4z" fill="var(--blue)"/></svg>
    <span>PO BOX 482<br>Elmwood North 3190,<br>Melbourne</span>
  </div>
  <div class="abs contact contact--mail">
    <svg width="11" height="8" viewBox="0 0 11 8"><rect width="11" height="8" fill="var(--blue)"/><path d="M0 0l5.5 4L11 0" fill="none" stroke="var(--navy)" stroke-width="1"/></svg>
    <span>hello@simplytuckaway.com.au</span>
  </div>
  <div class="abs contact contact--social">
    <svg width="8" height="8" viewBox="0 0 8 8"><circle cx="4" cy="4" r="4" fill="var(--blue)"/></svg>
    <span>simplytuckaway</span>
  </div>
  <p class="abs tagline tagline--back">Simply Tuck AWAY!</p>

  <div class="abs footer footer--back"><span>WWW.SIMPLYTUCKAWAY.COM.AU</span><span>1300 482 615</span></div>
  <div class="abs brand brand--small"><span class="brand__square"></span>Tuck Away!</div>
</section>

</body>
</html>
```